Business Card Design Project

I am a Chiropractor that is looking for a new business card.  Our logo was slightly changed lately, therefore need a new, more professional look.
We are a modern, non-stuffy chiropractic office.  Want a contemporary look that will let people know this is not your typical doctors office.  Our logo is red, and contains the name of our business: realign.  The u in the logo is green, stressing the most important part of our business: "u"

Target Market(s)
moderate to upper income bracket, family friendly
www.realignspine-example.com
Gordon Pell
Family Chiropractor
314 Hollis Rd
Carrow, NM 88999
512.555.0147 phone
512.555.0148 fax
Industry/Entity Type
Business
Requirements
Must have
- www.realignspine-example.com
Gordon Pell
Family Chiropractor
314 Hollis Rd
Carrow, NM 88999
512.555.0147 phone
512.555.0148 fax

```html
<!DOCTYPE html>
<html lang="en">
<head>
<meta charset="utf-8">
<title>Gordon Pell – Family Chiropractor</title>
<link rel="stylesheet" href="https://fonts.googleapis.com/css2?family=Roboto+Condensed:wght@300;400;700&display=swap">
<style>
  :root {
    --page: #ffffff;
    --fresh-green: #63fd12;
    --bold-red: #ff2024;
    --text-light: #ffffff;
  }
  * { margin: 0; padding: 0; box-sizing: border-box; }
  html, body {
    width: 1200px;
    height: 717px;
    overflow: hidden;
    background: var(--page);
  }
  .business-card {
    position: absolute;
    left: 22px;
    top: 24px;
    width: 1158px;
    height: 670px;
    border-radius: 50px;
    overflow: hidden;
    display: flex;
    font-family: "Roboto Condensed", "Arial Narrow", sans-serif;
    color: var(--text-light);
  }
  .brand-panel {
    width: 466px;
    background: var(--fresh-green);
    display: flex;
    align-items: center;
    justify-content: center;
  }
  .brand-name {
    font-size: 84px;
    font-weight: 400;
    color: var(--bold-red);
    letter-spacing: 1px;
  }
  .contact-panel {
    flex: 1;
    background: var(--bold-red);
    position: relative;
    text-align: center;
  }
  .contact-panel > * {
    position: absolute;
    left: 0;
    right: 0;
    line-height: 40px;
    letter-spacing: 0.5px;
  }
  .person-name {
    top: 92px;
    font-size: 34px;
    font-weight: 700;
  }
  .person-title {
    top: 137px;
    font-size: 37px;
    font-weight: 300;
  }
  .website {
    top: 311px;
    font-size: 31px;
    font-weight: 300;
  }
  .address {
    top: 446px;
    font-size: 34px;
    font-weight: 300;
    font-style: normal;
  }
</style>
</head>
<body>
  <main class="business-card">
    <section class="brand-panel">
      <span class="brand-name">realign</span>
    </section>
    <section class="contact-panel">
      <h1 class="person-name">Gordon Pell</h1>
      <p class="person-title">Family Chiropractor</p>
      <p class="website">www.realignspine-example.com</p>
      <address class="address">
        314 Hollis Rd<br>
        Carrow, NM 88999<br>
        Phone: 512.555.0147<br>
        Fax: 512.555.0148
      </address>
    </section>
  </main>
</body>
</html>
```